Business Card Design Project

Hi,
This is a simple contest. The logo for the back of the card is deigned. See attached files. The front of the card must have :

Directors Name: Dorian
Mob:
e-mail:
Postal Address:
Web Page Adress:

It may also add words: "Leaders in Construction Project Management Services"

Target Market(s)

Business & Home owners alike

Industry/Entity Type

Business

Requirements
Must have
• See details above and logo attached
Should not have
• Images other than logo

```html
<!DOCTYPE html>
<html lang="en">
<head>
<meta charset="utf-8">
<title>Keystone Works Pacific – Business Card</title>
<link rel="stylesheet" href="https://fonts.googleapis.com/css2?family=Questrial&display=swap">
<style>
  :root {
    --bg: #e9e6e1;
    --brand-blue: #0a97d6;
    --card-white: #ececec;
    --text-blue: #1b8fcf;
    --white: #ffffff;
    --shadow: rgba(0, 0, 0, 0.28);
  }
  * { margin: 0; padding: 0; box-sizing: border-box; }
  html, body {
    width: 1200px;
    height: 923px;
    overflow: hidden;
    background: var(--bg);
    font-family: "Questrial", "Century Gothic", sans-serif;
  }
  .stage { position: relative; width: 1200px; height: 923px; }

  .card {
    position: absolute;
    width: 590px;
    height: 340px;
    border-radius: 12px;
    box-shadow: 0 6px 18px var(--shadow);
    overflow: hidden;
  }

  /* Back side: solid blue with brand name */
  .card--back {
    left: 70px;
    top: 90px;
    background: var(--brand-blue);
    display: flex;
    align-items: center;
    justify-content: center;
  }

  .brand {
    display: flex;
    align-items: center;
    gap: 12px;
    color: var(--white);
    font-weight: 400;
    line-height: 1;
  }
  .brand__mark {
    width: 40px;
    height: 40px;
    background: var(--white);
  }
  .brand__name { display: flex; flex-direction: column; gap: 4px; }
  .brand__primary { font-size: 34px; letter-spacing: 1px; }
  .brand__secondary { font-size: 11.5px; letter-spacing: 3.2px; }

  .brand--small .brand__mark { width: 32px; height: 32px; }
  .brand--small .brand__primary { font-size: 26px; }
  .brand--small .brand__secondary { font-size: 9px; letter-spacing: 2.5px; }

  /* Front side: details */
  .card--front {
    left: 440px;
    top: 457px;
    background: var(--card-white);
  }
  .card__band {
    position: absolute;
    left: 0;
    top: 55px;
    width: 100%;
    height: 86px;
    background: var(--brand-blue);
    box-shadow: 0 2px 3px rgba(0, 0, 0, 0.18);
    display: flex;
    align-items: center;
    padding-left: 45px;
  }

  .contact {
    position: absolute;
    left: 204px;
    top: 200px;
    display: flex;
    color: var(--text-blue);
  }
  .contact__name {
    font-size: 19px;
    letter-spacing: 0.5px;
    padding-right: 9px;
    padding-top: 3px;
    text-transform: uppercase;
  }
  .contact__details {
    list-style: none;
    border-left: 1px solid var(--text-blue);
    padding-left: 10px;
    font-size: 12.5px;
    line-height: 15.5px;
  }

  .card__tagline {
    position: absolute;
    left: 0;
    width: 100%;
    top: 302px;
    text-align: center;
    font-size: 14.5px;
    color: var(--text-blue);
  }
</style>
</head>
<body>
  <main class="stage">
    <section class="card card--back" aria-label="Card back">
      <div class="brand">
        <span class="brand__mark"></span>
        <span class="brand__name">
          <span class="brand__primary">KEYSTONE</span>
          <span class="brand__secondary">WORKS PACIFIC</span>
        </span>
      </div>
    </section>

    <section class="card card--front" aria-label="Card front">
      <header class="card__band">
        <div class="brand brand--small">
          <span class="brand__mark"></span>
          <span class="brand__name">
            <span class="brand__primary">KEYSTONE</span>
            <span class="brand__secondary">WORKS PACIFIC</span>
          </span>
        </div>
      </header>

      <div class="contact">
        <p class="contact__name">Dorian</p>
        <ul class="contact__details">
          <li>Mob:</li>
          <li>e-mail:</li>
          <li>Postal Address:</li>
          <li>Web Page Adress:</li>
        </ul>
      </div>

      <p class="card__tagline">Leaders in Construction Project Management Services</p>
    </section>
  </main>
</body>
</html>
```